Copper Lantern Gatherings need a stand out marketing flyer.

Copper Lantern Gatherings is a company that runs empowerment retreats and bespoke corporate training in creating positive change.
We would like an A5 flyer that is 2 sided. the reverse side of the flyer we would like some of our testimonial quotes.

The flyer should be punchy and not too heavy with wordy detail but have enough detail so people can see what we offer. Encouraging people to contact us to find out more

Our empowerment retreats help people to live without limits, be fierce and wild, be creative and courageous, be fearless and free.
Leave behind
- lack of self esteem
- lack of personal power
- lack of focus
- old fears and beliefs
- overwhelm
Find new
- confidence
- personal empowerment
- commitment
- courage
- resilience

Contact details:
website: www.copperlanterngatherings.example.co.uk
email: info@copperlanterngatherings.example.com
Rebecca Thornby Tel: 07700 900 318
Joanna Pelling Tel: 07700 900 752

You can use as much of the detail above in your design as you would like..
I attach our logos. you can pick which ever design you prefer to work with. I have also attached a file that contains the testimonials for the reverse of the slide. I've also attached a few pictures but these aren't necessary in your design they are just an option/idea for you to consider. You can use alternative pictures should you wish to.

Details for our up and coming events can be found on our website

```html
<!DOCTYPE html>
<html lang="en">
<head>
<meta charset="utf-8">
<title>Copper Lantern Gatherings – Flyer</title>
<link href="https://fonts.googleapis.com/css2?family=Source+Sans+3:ital,wght@0,400;0,600;1,600&display=swap" rel="stylesheet">
<style>
  :root{
    --page-bg:#d5d6d8;
    --deep-blue:#0062c9;
    --mid-blue:#0a8fdc;
    --cyan:#00d6ff;
    --label-blue:#13a5e3;
    --brand-blue:#0b6fd9;
    --ink:#3a3a3a;
    --white:#ffffff;
    --black:#000000;
  }
  *{margin:0;padding:0;box-sizing:border-box}
  html,body{width:1200px;height:847px;overflow:hidden;background:var(--page-bg)}
  body{position:relative;font-family:"Source Sans 3",sans-serif}
  .side{position:absolute;top:23px;width:564.4px;height:801px;overflow:hidden}
  .side--front{left:25.6px;background:var(--white)}
  .side--back{left:610px;background:var(--black)}
  .side__art{position:absolute;left:0;top:0;width:100%;height:100%}
  .brand{position:absolute;left:0;width:100%;text-align:center;color:var(--brand-blue);font-weight:600}
  .brand__mark{width:56px;height:56px;border-radius:50%;background:var(--brand-blue);margin:0 auto 14px}
  .brand__name{font-size:30px;line-height:1.1;letter-spacing:.5px}
  .brand--front{top:92px}
  .brand--back{top:505px}
  .mission{position:absolute;left:0;top:335px;width:100%;text-align:center;color:var(--white);font-weight:600;font-size:14.6px;line-height:18.5px}
  .label{position:absolute;height:25.5px;background:var(--label-blue);color:var(--white);font-weight:600;font-size:15.5px;line-height:25.5px;text-align:center}
  .label--leave{left:53.8px;top:404.5px;width:135.4px}
  .label--find{left:323.4px;top:404.5px;width:135.4px}
  .label--contact{left:53.8px;top:620px;width:133.6px}
  .divider{position:absolute;left:280.5px;top:404.5px;width:3.2px;height:185px;background:var(--label-blue)}
  .checklist{position:absolute;top:445px;list-style:none;color:var(--ink);font-size:14.6px;line-height:27.1px}
  .checklist li{position:relative;padding-left:11px}
  .checklist li::before{content:"";position:absolute;left:0;top:12px;width:5px;height:5px;border-radius:50%;background:var(--label-blue)}
  .checklist--leave{left:55px}
  .checklist--find{left:324.6px}
  .contact{position:absolute;left:53.8px;top:651px;color:var(--ink);font-size:14.6px;line-height:22.5px}
  .testimonials{position:absolute;left:58px;top:87px;width:448px;color:var(--white);font-style:italic;font-weight:600;font-size:15.2px;line-height:19px;text-align:justify}
  .testimonials p{margin-bottom:19px}
</style>
</head>
<body>

<section class="side side--front">
  <svg class="side__art" viewBox="0 0 1080 1533" preserveAspectRatio="none" aria-hidden="true">
    <defs>
      <linearGradient id="frontTop" gradientUnits="userSpaceOnUse" x1="700" y1="0" x2="120" y2="360">
        <stop offset="0" stop-color="#0062c9"/><stop offset=".55" stop-color="#0a8fdc"/><stop offset="1" stop-color="#00d6ff"/>
      </linearGradient>
      <linearGradient id="frontBottom" gradientUnits="userSpaceOnUse" x1="400" y1="1533" x2="1000" y2="1180">
        <stop offset="0" stop-color="#0062c9"/><stop offset=".55" stop-color="#0a8fdc"/><stop offset="1" stop-color="#00d6ff"/>
      </linearGradient>
      <linearGradient id="band" x1="0" y1="0" x2="0" y2="1">
        <stop offset="0" stop-color="#0062c9"/><stop offset="1" stop-color="#00d6ff"/>
      </linearGradient>
    </defs>
    <path d="M0,0 H1080 V76 C700,60 250,120 0,352 Z" fill="url(#frontTop)"/>
    <path d="M0,258 C260,95 700,36 1080,48" fill="none" stroke="#fff" stroke-width="9"/>
    <path d="M0,1533 H1080 V1181 C830,1400 420,1470 0,1456 Z" fill="url(#frontBottom)"/>
    <path d="M1080,1291 C820,1455 420,1495 0,1483" fill="none" stroke="#fff" stroke-width="9"/>
    <rect x="0" y="617" width="1080" height="120" fill="url(#band)"/>
  </svg>

  <div class="brand brand--front">
    <div class="brand__mark"></div>
    <div class="brand__name">Copper Lantern<br>Gatherings</div>
  </div>

  <p class="mission">Our empowerment retreats help people to live without limits, be fierce<br>and wild, be creative and courageous, be fearless and free.</p>

  <div class="label label--leave">Leave behind</div>
  <div class="divider"></div>
  <div class="label label--find">Find new</div>

  <ul class="checklist checklist--leave">
    <li>Lack of self esteem</li>
    <li>Lack of personal power</li>
    <li>Lack of focus</li>
    <li>Old fears and beliefs</li>
    <li>Overwhelm</li>
  </ul>
  <ul class="checklist checklist--find">
    <li>Confidence</li>
    <li>Personal empowerment</li>
    <li>Commitment</li>
    <li>Courage</li>
    <li>Resilience</li>
  </ul>

  <div class="label label--contact">Contact details</div>
  <div class="contact">
    website: www.copperlanterngatherings.example.co.uk<br>
    email: info@copperlanterngatherings.example.com<br>
    Rebecca Thornby Tel: 07700 900 318<br>
    Joanna Pelling Tel: 07700 900 752
  </div>
</section>

<section class="side side--back">
  <svg class="side__art" viewBox="0 0 1080 1533" preserveAspectRatio="none" aria-hidden="true">
    <defs>
      <linearGradient id="backTop" gradientUnits="userSpaceOnUse" x1="380" y1="0" x2="960" y2="360">
        <stop offset="0" stop-color="#0062c9"/><stop offset=".55" stop-color="#0a8fdc"/><stop offset="1" stop-color="#00d6ff"/>
      </linearGradient>
      <linearGradient id="backBottom" gradientUnits="userSpaceOnUse" x1="680" y1="1533" x2="80" y2="1180">
        <stop offset="0" stop-color="#0062c9"/><stop offset=".55" stop-color="#0a8fdc"/><stop offset="1" stop-color="#00d6ff"/>
      </linearGradient>
    </defs>
    <path d="M1080,0 H0 V76 C380,60 830,120 1080,352 Z" fill="url(#backTop)"/>
    <path d="M1080,258 C820,95 380,36 0,48" fill="none" stroke="#000" stroke-width="9"/>
    <path d="M1080,1533 H0 V1181 C250,1400 660,1470 1080,1456 Z" fill="url(#backBottom)"/>
    <path d="M0,1291 C260,1455 660,1495 1080,1483" fill="none" stroke="#000" stroke-width="9"/>
  </svg>

  <div class="testimonials">
    <p>Do not hesitate, just book it! It will transform and<br>enhance your life.</p>
    <p>If you have a chance to do it then do it, it’s one of the best experience of my life.</p>
    <p>The most wonderful weekend of self-discovery and would recommend it to everyone.</p>
    <p>I’ve met the most amazing people and feel like I am well equipped with the tools now to help myself physically and mentally. The best self-care I’ve ever invested in.</p>
    <p>It’s changed my life, given me perspective and time to develop myself. I’ve met the most amazing people and learnt so much. It’s worth every penny.</p>
    <p>I can’t thank Copper Lantern enough for the tools they have metaphorically equipped me with. They are amazing at what they do.</p>
  </div>

  <div class="brand brand--back">
    <div class="brand__mark"></div>
    <div class="brand__name">Copper Lantern<br>Gatherings</div>
  </div>
</section>

</body>
</html>
```